Word document template for sales proposals

I am after a template that is simple but impactful. Use of colour to be limited but some for impact would be good. The proposals are for use in the professional technical field.

```html
<!DOCTYPE html>
<html lang="en">
<head>
<meta charset="utf-8">
<title>Brightwater Technical – Letterhead</title>
<link href="https://fonts.googleapis.com/css2?family=Lexend:wght@400;600&display=swap" rel="stylesheet">
<style>
  :root {
    --blue: #4bb5e3;
    --blue-deep: #3faedc;
    --orange: #f5a03c;
    --orange-deep: #ee9a35;
    --paper: #f1f1f1;
    --ink: #333333;
    --ink-strong: #262626;
    --signature-tone: #dcdcdc;
  }
  html, body {
    margin: 0;
    padding: 0;
    width: 848px;
    height: 1200px;
    overflow: hidden;
  }
  body {
    background: var(--paper);
    font-family: "Lexend", sans-serif;
    color: var(--ink);
  }
  .letterhead {
    position: relative;
    width: 848px;
    height: 1200px;
    background: var(--paper);
  }
  .band { position: absolute; left: 0; width: 100%; }
  .band--top-blue { top: 0; height: 30px; background: var(--blue); }
  .band--top-orange { top: 30px; height: 14px; background: var(--orange); }
  .band--bottom-orange { top: 1131px; height: 27px; background: var(--orange-deep); }
  .band--bottom-blue { top: 1158px; height: 42px; background: var(--blue-deep); }

  .brand {
    position: absolute;
    left: 44px;
    top: 78px;
    width: 220px;
    text-align: center;
  }
  .brand__dot {
    display: block;
    width: 62px;
    height: 62px;
    margin: 0 auto 20px;
    border-radius: 50%;
    background: var(--blue);
  }
  .brand__name {
    font-weight: 600;
    font-size: 19px;
    letter-spacing: 0.5px;
    color: var(--orange);
    white-space: nowrap;
  }

  .sender {
    position: absolute;
    left: 49px;
    top: 251px;
    font-style: normal;
    font-size: 14.5px;
    letter-spacing: 0.3px;
    line-height: 23.5px;
  }
  .date {
    position: absolute;
    right: 51px;
    top: 234px;
    font-size: 15.5px;
    letter-spacing: 0.3px;
  }

  .letter-body {
    position: absolute;
    left: 49px;
    top: 394px;
    width: 724px;
  }
  .salutation {
    margin: 0 0 8px;
    font-weight: 600;
    font-size: 15.5px;
    letter-spacing: 0.4px;
    line-height: 20px;
    color: var(--ink-strong);
  }
  .letter-body p {
    margin: 0;
    font-size: 15.5px;
    letter-spacing: 0.5px;
    line-height: 21.4px;
    text-align: justify;
  }
  .letter-body p + p { margin-top: 43px; }

  .sign-off {
    position: absolute;
    left: 53px;
    top: 858px;
    width: 180px;
  }
  .sign-off__closing {
    margin: 0 0 0 28px;
    font-weight: 600;
    font-size: 17.5px;
    letter-spacing: 0.5px;
    color: var(--ink-strong);
  }
  .sign-off__signature {
    width: 168px;
    height: 66px;
    margin-top: 6px;
    background: linear-gradient(90deg, var(--signature-tone), #e8e8e8);
    border-radius: 4px;
  }
  .sign-off__name {
    margin: 8px 0 0 26px;
    font-size: 16.5px;
    letter-spacing: 0.4px;
  }

  .contact {
    position: absolute;
    left: 517px;
    top: 857px;
  }
  .contact__title {
    margin: 0 0 12px;
    font-weight: 600;
    font-size: 17.5px;
    letter-spacing: 0.5px;
    color: var(--ink-strong);
  }
  .contact__list { list-style: none; margin: 0; padding: 0; }
  .contact__item {
    display: flex;
    align-items: center;
    height: 27px;
    font-size: 16.5px;
    letter-spacing: 0.4px;
    white-space: nowrap;
  }
  .contact__icon {
    width: 15px;
    height: 15px;
    margin: 0 10px 0 1px;
    fill: #444;
  }
</style>
</head>
<body>
<main class="letterhead">
  <div class="band band--top-blue"></div>
  <div class="band band--top-orange"></div>

  <header class="brand">
    <span class="brand__dot"></span>
    <div class="brand__name">BRIGHTWATER TECHNICAL</div>
  </header>

  <address class="sender">
    48 Harbour Lane, &nbsp;Westford, NV 20451<br>
    bwtech.com<br>
    +1-555-014-2290
  </address>
  <div class="date">December 14, 2023</div>

  <section class="letter-body">
    <h2 class="salutation">Dear Mr. Marcus Whitfield</h2>
    <p>A &nbsp;letterhead is the heading at the top of a sheet of letter paper (stationery).<br>
    That heading usually consists of a name and an address, and a logo or corporate design, and sometimes a background pattern. The term "letterhead" is often used to refer to the whole sheet imprinted with such a heading. Many companies and individuals prefer to create a letterhead template in a word processor or other software application.</p>
    <p>This generally includes the same information as pre-printed stationery but without the additional costs involved. Letterhead can then be printed on stationery (or plain paper) as needed on a local output device or sent electronically.</p>
    <p>The term "letterhead" is often used to refer to the whole sheet imprinted with such a heading. Many companies and individuals prefer to create a letterhead template in a word processor or other software application.</p>
  </section>

  <section class="sign-off">
    <p class="sign-off__closing">Best Regards,</p>
    <div class="sign-off__signature" role="img" aria-label="Handwritten signature of Jordan Ellery"></div>
    <p class="sign-off__name">Jordan Ellery</p>
  </section>

  <section class="contact">
    <h3 class="contact__title">Our Contact</h3>
    <ul class="contact__list">
      <li class="contact__item">
        <svg class="contact__icon" viewBox="0 0 16 16" aria-hidden="true"><path d="M1 3h14v10H1z"/><path d="M1.5 3.5 8 8.2l6.5-4.7" fill="none" stroke="#f1f1f1" stroke-width="1.3"/></svg>
        mail.bwtech.com
      </li>
      <li class="contact__item">
        <svg class="contact__icon" viewBox="0 0 16 16" aria-hidden="true"><circle cx="8" cy="8" r="7"/><g fill="none" stroke="#f1f1f1" stroke-width="1"><ellipse cx="8" cy="8" rx="3" ry="7"/><path d="M1 8h14M2 4.5h12M2 11.5h12"/></g></svg>
        @bwtech
      </li>
      <li class="contact__item">
        <svg class="contact__icon" viewBox="0 0 16 16" aria-hidden="true"><path d="M8 1a5 5 0 0 0-5 5c0 3.8 5 9 5 9s5-5.2 5-9a5 5 0 0 0-5-5z"/><circle cx="8" cy="6" r="1.9" fill="#f1f1f1"/></svg>
        Westford, 48 Harbour Ln
      </li>
    </ul>
  </section>

  <div class="band band--bottom-orange"></div>
  <div class="band band--bottom-blue"></div>
</main>
</body>
</html>
```